Printing company needs stellar web site!

We need a website for a printing company based in Atlanta, Georgia, USA. Our company is 26 years old and just this year did a logo and branding refresh. Now we need our website to be refreshed as well.

Please see the attached source files for our new logo and stationary design.

Printing

```html
<!DOCTYPE html>
<html lang="en">
<head>
<meta charset="utf-8">
<title>Kestrel Print, Inc.</title>
<link rel="stylesheet" href="https://fonts.googleapis.com/css2?family=Ubuntu:wght@300;400;500;700&family=Arvo:wght@700&family=Open+Sans:wght@400&display=swap">
<style>
:root{
  --blue:#0b6fc1;
  --blue-dark:#0a4f94;
  --logo-blue:#1762ad;
  --ink:#333;
  --muted:#555;
  --grey-band:#ebebeb;
  --card:#e8e8e8;
  --line:#cfcfcf;
  --white:#fff;
}
*{margin:0;padding:0;box-sizing:border-box}
html,body{width:1200px;height:2184px;overflow:hidden}
body{position:relative;background:var(--white);font-family:"Open Sans",sans-serif;color:var(--ink)}
.abs{position:absolute}

/* header */
.brand{left:18px;top:24px;display:flex;align-items:center;gap:12px}
.brand-dot{width:44px;height:44px;border-radius:50%;background:var(--logo-blue)}
.brand-name{font-family:"Ubuntu",sans-serif;font-weight:700;font-size:48px;color:var(--logo-blue);letter-spacing:1px;line-height:1}
.call{right:126px;top:28px;font-family:"Ubuntu",sans-serif;color:var(--blue);font-size:29px;font-weight:400}
.call strong{font-weight:700;font-size:31px}
.social{right:24px;top:31px;display:flex;gap:8px}
.social span{width:34px;height:34px;border-radius:4px;background:var(--logo-blue)}

/* nav */
.nav{left:0;top:98px;width:1200px;height:48px;background:var(--blue);display:flex}
.nav a{display:flex;align-items:center;justify-content:center;height:48px;color:var(--white);font-family:"Ubuntu",sans-serif;font-weight:500;font-size:15px;text-decoration:none;border-right:1px solid #0a5ea6}

/* hero */
.hero{left:0;top:146px;width:1200px;height:530px;background:linear-gradient(100deg,#f28a1c 0%,#e9543a 14%,#ddd 30%,#c9c9c9 55%,#e3d7cf 70%,#9bb3d8 85%,#d3c4e0 100%)}
.hero-band{left:0;top:457px;width:909px;height:147px;background:rgba(38,140,214,.78);padding:14px 0 0 28px;color:var(--white)}
.hero-band h1{font-family:"Arvo",serif;font-weight:700;font-size:36px;line-height:42px}
.hero-band p{font-family:"Ubuntu",sans-serif;font-size:27px;margin-top:6px}

/* welcome */
.welcome{left:60px;top:694px;width:1080px;text-align:center}
.section-title{font-family:"Ubuntu",sans-serif;font-weight:300;font-size:35px;color:#444}
.welcome p{font-size:12.5px;line-height:19px;color:var(--muted);margin-top:17px}
.welcome .section-title{margin-bottom:8px}

/* markets */
.markets{left:0;top:897px;width:1200px;height:335px;background:var(--grey-band)}
.markets .section-title{position:absolute;top:30px;width:1200px;text-align:center}
.market{position:absolute;top:90px;width:200px;text-align:center;font-family:"Ubuntu",sans-serif;font-size:15px;color:#444;line-height:19px}
.market-icon{width:164px;height:164px;margin:0 auto 14px;border-radius:50%;border:5px solid var(--white);background:radial-gradient(circle at 50% 30%,#bfe3fb 0%,#4aa3e6 55%,#1b78c7 100%);box-shadow:0 2px 5px rgba(0,0,0,.2)}

/* lower columns */
.col-title{font-family:"Ubuntu",sans-serif;font-weight:400;font-size:25px;color:#444;display:flex;align-items:center;gap:12px}
.col-title em{font-style:normal;color:var(--blue)}
.services{left:62px;top:1274px}
.service-list{list-style:none;margin:20px 0 0 56px}
.service-list li{display:flex;align-items:center;gap:14px;height:28.8px;font-size:13.5px;color:var(--muted)}
.testimonials{left:459px;top:1274px}
.quote{position:absolute;left:459px;width:307px;height:141px;background:var(--card);border-radius:4px;padding:16px 18px;font-size:12.5px;line-height:18.5px;color:var(--muted)}
.quote .author{display:flex;align-items:center;gap:10px;margin-top:10px;font-family:"Ubuntu",sans-serif;font-size:14px;color:#444}
.callback{left:854px;top:1274px}
.field{position:absolute;left:857px;width:253px;height:30px;border:1px solid #bbb;border-radius:3px;background:var(--white);font-size:11.5px;color:#777;padding:6px 7px}
.submit{left:857px;top:1453px;width:91px;height:32px;background:var(--blue);color:var(--white);font-family:"Ubuntu",sans-serif;font-weight:700;font-size:12.5px;display:flex;align-items:center;justify-content:center;border-radius:2px}
.badge{left:857px;top:1519px;width:245px;height:113px;border-radius:6px;background:linear-gradient(#f0d58a,#c89a3a);padding:6px}
.badge div{width:100%;height:100%;border-radius:3px;background:#8c1b3c}
.badge-caption{left:857px;top:1636px;width:245px;text-align:center;font-family:"Ubuntu",sans-serif;font-weight:500;font-size:18px;color:#a0203f}

/* contact */
.contact-title{left:70px;top:1722px}
.contact-col{position:absolute;top:1794px;font-size:12px;line-height:18.4px;color:var(--muted)}
.contact-col h4{font-family:"Ubuntu",sans-serif;font-weight:400;font-size:14.5px;color:#333;margin-bottom:3px}
.contact-col h4.gap{margin-top:8px}

/* footer */
.footer-wave{left:0;top:1900px;width:1200px;height:284px}
.footer-nav{left:28px;top:2101px;display:flex;gap:16px;font-family:"Ubuntu",sans-serif;font-weight:500;font-size:15px;color:var(--white)}
.copyright{left:28px;top:2125px;font-size:11.5px;color:#e4efff}
.footer-brand{right:34px;top:2100px;display:flex;align-items:center;gap:12px}
.footer-brand .brand-dot{background:var(--white);width:42px;height:42px}
.footer-brand .brand-name{color:var(--white);font-size:46px}
</style>
</head>
<body>

<header>
  <div class="abs brand"><span class="brand-dot"></span><span class="brand-name">KESTREL</span></div>
  <div class="abs call">Call : <strong>555.210.4480</strong></div>
  <div class="abs social"><span></span><span></span><span></span></div>
</header>

<nav class="abs nav">
  <a style="width:91px">Home</a>
  <a style="width:118px">Markets</a>
  <a style="width:114px">Products</a>
  <a style="width:118px">Services</a>
  <a style="width:118px">About Us</a>
  <a style="width:123px">Contact Us</a>
  <a style="width:177px">Customer Services</a>
  <a style="width:120px">FTP Login</a>
</nav>

<section class="abs hero" role="img" aria-label="Hand holding a magnifying loupe over a colour proof beside a fanned colour swatch guide"></section>
<div class="abs hero-band">
  <h1>We know, We understand,<br>We will exceed your expectations</h1>
  <p>Since 1989, A Leader in the Label Industry in Product and Service!</p>
</div>

<section class="abs welcome">
  <h2 class="section-title">Welcome to Kestrel Print, Inc.</h2>
  <p>Kestrel Print, Inc. is located in Lakeside, Georgia, just north of downtown Atlanta. Kestrel Print's 45,000 sq. ft. facility is strategically located close to the transportation hub<br>of the southeast which enables us to efficiently deliver your product anywhere around the globe.</p>
  <p>We understand that your product cannot leave until the label is on it; the close interaction of our departments ensures your order is produced to your exact specifications<br>and delivered to your door on time.</p>
  <p>Over the years, Kestrel Print has become one of the label industry's leaders in offering outstanding service, quality product, and competitive pricing.</p>
</section>

<section class="abs markets">
  <h2 class="section-title">Markets Served</h2>
  <div class="market" style="left:160px"><div class="market-icon" role="img" aria-label="Burger illustration"></div>Food &amp; Beverage<br>Industry</div>
  <div class="market" style="left:385px"><div class="market-icon" role="img" aria-label="Medical chart illustration"></div>Health &amp; Beauty<br>Industry</div>
  <div class="market" style="left:610px"><div class="market-icon" role="img" aria-label="Laboratory flask illustration"></div>Chemical<br>Industry</div>
  <div class="market" style="left:835px"><div class="market-icon" role="img" aria-label="Hanging tag illustration"></div>Specialty<br>Labels</div>
</section>

<section class="abs services">
  <h3 class="col-title">
    <svg width="46" height="46" viewBox="0 0 46 46" aria-hidden="true"><g fill="none" stroke="#555" stroke-width="3"><circle cx="16" cy="16" r="8"/><circle cx="16" cy="16" r="3"/><circle cx="33" cy="33" r="6"/><circle cx="33" cy="33" r="2"/></g><g stroke="#555" stroke-width="4"><path d="M16 3v5M16 24v5M3 16h5M24 16h5M7 7l3 3M22 22l3 3M25 7l-3 3M7 25l3-3"/><path d="M33 24v3M33 39v3M24 33h3M39 33h3"/></g></svg>
    Services for you
  </h3>
  <ul class="service-list">
    <li><svg width="20" height="18" viewBox="0 0 20 18"><rect x="1" y="3" width="14" height="14" rx="3" fill="none" stroke="#444" stroke-width="2"/><path d="M4 9l4 4 10-11" fill="none" stroke="#444" stroke-width="2.5"/></svg>4 Color Process</li>
    <li><svg width="20" height="18" viewBox="0 0 20 18"><rect x="1" y="3" width="14" height="14" rx="3" fill="none" stroke="#444" stroke-width="2"/><path d="M4 9l4 4 10-11" fill="none" stroke="#444" stroke-width="2.5"/></svg>Color Matching</li>
    <li><svg width="20" height="18" viewBox="0 0 20 18"><rect x="1" y="3" width="14" height="14" rx="3" fill="none" stroke="#444" stroke-width="2"/><path d="M4 9l4 4 10-11" fill="none" stroke="#444" stroke-width="2.5"/></svg>Flexible Packaging</li>
    <li><svg width="20" height="18" viewBox="0 0 20 18"><rect x="1" y="3" width="14" height="14" rx="3" fill="none" stroke="#444" stroke-width="2"/><path d="M4 9l4 4 10-11" fill="none" stroke="#444" stroke-width="2.5"/></svg>Piggyback</li>
    <li><svg width="20" height="18" viewBox="0 0 20 18"><rect x="1" y="3" width="14" height="14" rx="3" fill="none" stroke="#444" stroke-width="2"/><path d="M4 9l4 4 10-11" fill="none" stroke="#444" stroke-width="2.5"/></svg>Two Side Print</li>
    <li><svg width="20" height="18" viewBox="0 0 20 18"><rect x="1" y="3" width="14" height="14" rx="3" fill="none" stroke="#444" stroke-width="2"/><path d="M4 9l4 4 10-11" fill="none" stroke="#444" stroke-width="2.5"/></svg>UV Printing</li>
    <li><svg width="20" height="18" viewBox="0 0 20 18"><rect x="1" y="3" width="14" height="14" rx="3" fill="none" stroke="#444" stroke-width="2"/><path d="M4 9l4 4 10-11" fill="none" stroke="#444" stroke-width="2.5"/></svg>UV Varnish</li>
    <li><svg width="20" height="18" viewBox="0 0 20 18"><rect x="1" y="3" width="14" height="14" rx="3" fill="none" stroke="#444" stroke-width="2"/><path d="M4 9l4 4 10-11" fill="none" stroke="#444" stroke-width="2.5"/></svg>Gloss and Matte Laminate</li>
    <li><svg width="20" height="18" viewBox="0 0 20 18"><rect x="1" y="3" width="14" height="14" rx="3" fill="none" stroke="#444" stroke-width="2"/><path d="M4 9l4 4 10-11" fill="none" stroke="#444" stroke-width="2.5"/></svg>Labels</li>
    <li><svg width="20" height="18" viewBox="0 0 20 18"><rect x="1" y="3" width="14" height="14" rx="3" fill="none" stroke="#444" stroke-width="2"/><path d="M4 9l4 4 10-11" fill="none" stroke="#444" stroke-width="2.5"/></svg>Specility Label Constructions</li>
    <li><svg width="20" height="18" viewBox="0 0 20 18"><rect x="1" y="3" width="14" height="14" rx="3" fill="none" stroke="#444" stroke-width="2"/><path d="M4 9l4 4 10-11" fill="none" stroke="#444" stroke-width="2.5"/></svg>Label Substrates</li>
    <li><svg width="20" height="18" viewBox="0 0 20 18"><rect x="1" y="3" width="14" height="14" rx="3" fill="none" stroke="#444" stroke-width="2"/><path d="M4 9l4 4 10-11" fill="none" stroke="#444" stroke-width="2.5"/></svg>Tooling Types</li>
  </ul>
</section>

<section class="abs testimonials">
  <h3 class="col-title">
    <svg width="24" height="38" viewBox="0 0 24 38" aria-hidden="true"><rect x="2" y="2" width="20" height="34" rx="3" fill="none" stroke="#777" stroke-width="2"/><rect x="5" y="7" width="14" height="22" fill="none" stroke="#999" stroke-width="1"/><circle cx="12" cy="32" r="1.5" fill="#777"/></svg>
    What <em>Clients Say</em>
  </h3>
</section>
<blockquote class="quote" style="top:1337px">
  “ Sample text sample text sample text sample text sample text sample text sample text sample text sample text sample text sample text...”
  <div class="author"><svg width="18" height="18" viewBox="0 0 18 18"><circle cx="9" cy="5" r="4.5" fill="#555"/><path d="M1 18c0-6 4-8 8-8s8 2 8 8z" fill="#555"/></svg>Dana Whitfield</div>
</blockquote>
<blockquote class="quote" style="top:1496px">
  “ Sample text sample text sample text sample text sample text sample text sample text sample text sample text sample text sample text...”
  <div class="author"><svg width="18" height="18" viewBox="0 0 18 18"><circle cx="9" cy="5" r="4.5" fill="#555"/><path d="M1 18c0-6 4-8 8-8s8 2 8 8z" fill="#555"/></svg>Dana Whitfield</div>
</blockquote>

<section class="abs callback">
  <h3 class="col-title">
    <svg width="28" height="24" viewBox="0 0 28 24" aria-hidden="true"><path d="M2 8c0-4 6-6 12-6s12 2 12 6v2h-6V7c-3-1-9-1-12 0v3H2z" fill="#333"/><path d="M6 12h16l3 10H3z" fill="#333"/><circle cx="14" cy="17" r="3" fill="#fff"/></svg>
    Request a <em>Call back</em>
  </h3>
</section>
<div class="field" style="top:1335px">Name</div>
<div class="field" style="top:1373px">Phone No.</div>
<div class="field" style="top:1411px">Email Id</div>
<div class="abs submit">SUBMIT</div>
<div class="abs badge" role="img" aria-label="Trade association anniversary badge"><div></div></div>
<div class="abs badge-caption">PLA's Golden Anniversary</div>

<section>
  <h3 class="abs col-title contact-title">
    <svg width="46" height="44" viewBox="0 0 46 44" aria-hidden="true"><path d="M2 16L23 2l21 14v26H2z" fill="#c9302c"/><rect x="8" y="6" width="30" height="22" fill="#fff"/><path d="M2 16l21 14 21-14v26H2z" fill="#e0463f"/><path d="M2 42l21-14 21 14" fill="#b72a26"/></svg>
    Kestrel Print Contact Information
  </h3>
  <div class="contact-col" style="left:128px">
    <h4>Phone</h4>Toll Free 800.555.0199<br>Local 555.210.4480
    <h4 class="gap">Fax</h4>Local 555.210.4482
  </div>
  <div class="contact-col" style="left:324px">
    <h4>Email</h4>Sales - sales@kestrelprint.example<br>Customer Service - service@kestrelprint.example<br>Orders - orders@kestrelprint.example<br>Art - art@kestrelprint.example<br>Shipping - shipping@kestrelprint.example
  </div>
  <div class="contact-col" style="left:604px">
    <h4>Physical Address</h4>Kestrel Print, Inc.<br>1200 Ridgeway Park Drive<br>Lakeside, GA 30099
  </div>
  <div class="contact-col" style="left:849px">
    <h4>Mailing Address</h4>Kestrel Print, Inc.<br>POB 412<br>Lakeside, GA 30098
  </div>
</section>

<footer>
  <svg class="abs footer-wave" viewBox="0 0 1200 284" preserveAspectRatio="none" aria-hidden="true">
    <path d="M0 18 C300 120 800 140 1200 -10 L1200 284 L0 284 Z" fill="#0b5fae"/>
    <path d="M0 40 C350 130 850 150 1200 20 L1200 284 L0 284 Z" fill="#0c6cc0"/>
    <path d="M300 165 C650 190 950 150 1200 80 L1200 92 C950 170 650 205 300 165 Z" fill="#ffffff"/>
    <path d="M300 165 C650 205 950 170 1200 92 L1200 284 L0 284 L0 120 C100 150 200 160 300 165 Z" fill="#0b6fc1"/>
  </svg>
  <nav class="abs footer-nav"><span>Home</span><span>Markets</span><span>Products</span><span>Services</span><span>About Us</span><span>Contact Us</span><span>Customer Services</span></nav>
  <div class="abs copyright">Copyright © 2011, Kestrel Print, Inc. / www.kestrelprint-inc.example. All Rights Reserved.</div>
  <div class="abs footer-brand"><span class="brand-dot"></span><span class="brand-name">KESTREL</span></div>
</footer>

</body>
</html>
```